Talbrook landscape Solutions Postcard

Landscape Company, but we mainly focus on hardscape construction like stone walls and walkways, as well as our tree pruning. irrigation, weekly maintenance
I want the front of the postcard to draw u into the images and the back to have basic information

Reason: I need the card to have a backside and now be able to be mailed. I also need the images switched out. As well as some new verbage

Target Market(s)

High end home owners

Industry/Entity Type

Landscaping

Font styles to use
Decorative
Script

Requirements
Must have
• OUR SERVICES to be listed on the back as well as
• call for a free estimate
• follow us on chatlane and clipwall and roomvy
• Coupon outline
• New Customers Receive
• 10% off
• your hardscape project
• Decorate font for title on front of the card and coupon offer
Nice to have
• The front of the card should have a few of our images taking up the whole cover with our logo LOOK AT THE BECKET IMAGE I attached. I am going for that look with the classic black

```html
<!DOCTYPE html>
<html lang="en">
<head>
<meta charset="utf-8">
<title>Talbrook Landscape Solutions Postcard</title>
<link rel="stylesheet" href="https://fonts.googleapis.com/css2?family=Almendra+Display&family=Josefin+Sans:wght@400;600&family=Lato:ital,wght@0,400;0,700;1,700&family=Oswald:wght@500;700&display=swap">
<style>
:root{
  --backdrop:#e9ecef;
  --black:#0b0b0b;
  --ray:#171717;
  --gold:#e8a330;
  --gold-dark:#b9791c;
  --white:#ffffff;
  --green:#3aa935;
  --forest:#1d4d1f;
  --stone:#2a2a2a;
  --ink:#222222;
}
*{margin:0;padding:0;box-sizing:border-box}
html,body{width:900px;height:1200px;overflow:hidden;background:var(--backdrop)}
.canvas{position:relative;width:900px;height:1200px}
.postcard{position:absolute;overflow:hidden}
.postcard--front{left:97px;top:52px;width:706px;height:543px;background:var(--black)}
.postcard--back{left:91px;top:620px;width:718px;height:557px;background:var(--white)}
.rays{position:absolute;inset:0}
.postcard--front .rays{background:repeating-conic-gradient(from 0deg at 78% 46%,var(--ray) 0 5deg,var(--black) 5deg 10deg)}
.postcard--back .rays{right:330px;background:repeating-conic-gradient(from 0deg at 45% 30%,var(--ray) 0 5deg,var(--black) 5deg 10deg)}
.artwork{position:absolute;inset:0;width:100%;height:100%}
.logo-tab{position:absolute;background:var(--white);display:flex;align-items:center;justify-content:center}
.logo-tab__mark{background:var(--black);width:100%;height:100%;display:flex;align-items:center;justify-content:center;text-align:center;color:var(--white);font-family:'Josefin Sans',sans-serif;font-weight:400;letter-spacing:1px;line-height:1.25}
.postcard--front .logo-tab{left:586px;top:10px;width:98px;height:106px;padding:6px}
.postcard--front .logo-tab__mark{font-size:11px}
.postcard--back .logo-tab{left:141px;top:0;width:125px;height:148px;padding:42px 7px 8px}
.postcard--back .logo-tab__mark{font-size:13px}
.headline{position:absolute;left:470px;top:160px;width:196px;text-align:center;color:var(--white)}
.headline__lead{font-family:'Josefin Sans',sans-serif;font-size:17px;letter-spacing:1px;padding-bottom:8px;border-bottom:1px solid #8a8a8a}
.headline__title{font-family:'Almendra Display',serif;font-size:38px;line-height:1;margin-top:14px}
.headline__title--sub{font-size:31px;margin-top:4px;padding-bottom:12px;border-bottom:1px solid #8a8a8a}
.website{position:absolute;left:478px;top:470px;font-family:'Josefin Sans',sans-serif;font-weight:600;font-size:14px;letter-spacing:2px;color:var(--ink)}
.services__tag{position:absolute;left:84px;top:202px;width:225px;height:30px;border-radius:6px;background:var(--gold);font-family:'Lato',sans-serif;font-style:italic;font-weight:700;font-size:17px;color:var(--ink);text-align:center;line-height:30px}
.services__list{position:absolute;left:44px;top:240px;width:316px;list-style:none;display:grid;grid-template-columns:143px 150px;font-family:'Lato',sans-serif;font-size:17px;color:var(--white)}
.services__list li{position:relative;padding-left:13px;line-height:19px;height:28px;padding-top:3px}
.services__list li::before{content:"";position:absolute;left:0;top:10px;width:5px;height:5px;border-radius:50%;background:var(--green)}
.services__list .rule{border-bottom:1px solid var(--green)}
.services__list .tall{height:auto}
.contact{position:absolute;left:20px;top:385px;width:350px;text-align:center}
.contact__cta{font-family:'Oswald',sans-serif;font-weight:500;font-size:21px;color:var(--white);letter-spacing:.2px}
.contact__heading{font-family:'Oswald',sans-serif;font-weight:500;font-size:20px;color:var(--gold);margin-top:2px}
.contact__line{display:flex;align-items:center;justify-content:center;gap:8px;color:var(--white);font-family:'Lato',sans-serif}
.contact__line--email{font-size:13px;margin-top:6px}
.contact__line--phone{font-family:'Oswald',sans-serif;font-weight:500;font-size:21px;margin-top:2px}
.contact__social{font-family:'Lato',sans-serif;font-size:13px;color:var(--white);margin-top:4px}
.coupon{position:absolute;left:295px;top:265px;width:160px;height:160px}
.coupon__text{position:absolute;inset:0;display:flex;flex-direction:column;align-items:center;justify-content:center;font-family:'Oswald',sans-serif;font-weight:700;color:var(--forest);line-height:1}
.coupon__value{font-size:44px;letter-spacing:-1px}
.coupon__value small{font-size:22px;vertical-align:top}
.coupon__off{font-size:40px}
</style>
</head>
<body>
<main class="canvas">

  <section class="postcard postcard--front" aria-label="Postcard front">
    <div class="rays"></div>
    <svg class="artwork" viewBox="0 0 706 543" aria-hidden="false">
      <defs>
        <linearGradient id="gardenTones" x1="0" y1="0" x2="1" y2="1">
          <stop offset="0" stop-color="#d9dfe2"/>
          <stop offset=".35" stop-color="#7f9a5a"/>
          <stop offset=".7" stop-color="#a44a34"/>
          <stop offset="1" stop-color="#6f6a5c"/>
        </linearGradient>
        <linearGradient id="goldBand" x1="0" y1="0" x2="1" y2="0">
          <stop offset="0" stop-color="var(--gold-dark)"/>
          <stop offset=".5" stop-color="var(--gold)"/>
          <stop offset="1" stop-color="var(--gold-dark)"/>
        </linearGradient>
        <linearGradient id="stoneTones" x1="0" y1="0" x2="0" y2="1">
          <stop offset="0" stop-color="#3a3a3a"/>
          <stop offset="1" stop-color="#161616"/>
        </linearGradient>
        <linearGradient id="thumbA" x1="0" y1="0" x2="0" y2="1"><stop offset="0" stop-color="#e6ece8"/><stop offset="1" stop-color="#6e8f4a"/></linearGradient>
        <linearGradient id="thumbB" x1="0" y1="0" x2="0" y2="1"><stop offset="0" stop-color="#5b7a3a"/><stop offset="1" stop-color="#9c8a72"/></linearGradient>
        <linearGradient id="thumbC" x1="0" y1="0" x2="0" y2="1"><stop offset="0" stop-color="#dfe7ec"/><stop offset=".5" stop-color="#8d8a80"/><stop offset="1" stop-color="#5f8e3c"/></linearGradient>
      </defs>
      <polygon points="0,0 282,0 480,430 0,430" fill="url(#gardenTones)" role="img" aria-label="Photo of a red brick patio with a curved stone wall beside a shingled house"/>
      <polygon points="282,0 300,0 498,430 480,430" fill="#2b2b2b"/>
      <polygon points="290,0 350,0 505,430 495,430" fill="url(#goldBand)"/>
      <polygon points="350,0 372,0 512,430 505,430" fill="#1f1f1f"/>
      <rect x="470" y="424" width="236" height="9" fill="var(--gold)"/>
      <rect x="0" y="433" width="706" height="63" fill="var(--white)"/>
      <rect x="0" y="496" width="706" height="47" fill="url(#stoneTones)" role="img" aria-label="Dark stone wall texture"/>
      <g class="thumbnails">
        <rect x="75" y="373" width="120" height="95" fill="var(--white)"/>
        <rect x="80" y="378" width="110" height="85" fill="var(--black)"/>
        <rect x="88" y="384" width="94" height="73" fill="url(#thumbA)" role="img" aria-label="Photo of a lawn and planting beds"/>
        <rect x="214" y="373" width="120" height="95" fill="var(--white)"/>
        <rect x="219" y="378" width="110" height="85" fill="var(--black)"/>
        <rect x="227" y="384" width="94" height="73" fill="url(#thumbB)" role="img" aria-label="Photo of a garden arbor and gate"/>
        <rect x="348" y="373" width="120" height="95" fill="var(--white)"/>
        <rect x="353" y="378" width="110" height="85" fill="var(--black)"/>
        <rect x="361" y="384" width="94" height="73" fill="url(#thumbC)" role="img" aria-label="Photo of a fieldstone wall"/>
        <g stroke="#9a9a9a" stroke-width="1">
          <line x1="75" y1="473" x2="195" y2="473"/>
          <line x1="214" y1="473" x2="334" y2="473"/>
          <line x1="348" y1="473" x2="468" y2="473"/>
        </g>
      </g>
    </svg>
    <div class="logo-tab"><div class="logo-tab__mark">TALBROOK<br>Landscape<br>Solutions</div></div>
    <div class="headline">
      <p class="headline__lead">We mainly focus on</p>
      <h1 class="headline__title">Hardscape</h1>
      <p class="headline__title headline__title--sub">construction</p>
    </div>
    <p class="website">www.talbrookland.com</p>
  </section>

  <section class="postcard postcard--back" aria-label="Postcard back">
    <svg class="artwork" viewBox="0 0 718 557">
      <polygon points="0,0 378,0 362,557 0,557" fill="var(--black)"/>
      <polygon points="375,0 410,0 392,557 362,557" fill="var(--gold)"/>
      <polygon points="410,0 432,0 400,557 392,557" fill="#2a2a2a"/>
      <polygon points="334,523 718,523 718,557 320,557" fill="var(--green)"/>
      <rect x="592" y="37" width="92" height="100" fill="none" stroke="#555" stroke-width="1.5" stroke-dasharray="3 3"/>
      <rect x="598" y="43" width="80" height="88" fill="none" stroke="#555" stroke-width="1"/>
      <g stroke="#333" stroke-width="1.5">
        <line x1="462" y1="375" x2="692" y2="375"/>
        <line x1="462" y1="415" x2="692" y2="415"/>
        <line x1="462" y1="455" x2="692" y2="455"/>
        <line x1="462" y1="493" x2="692" y2="493"/>
      </g>
    </svg>
    <div class="rays" style="opacity:.0"></div>
    <div class="logo-tab"><div class="logo-tab__mark">TALBROOK<br>Landscape<br>Solutions</div></div>
    <h2 class="services__tag">Our Services:</h2>
    <ul class="services__list">
      <li class="rule">Stone walls</li>
      <li class="rule">Walkways</li>
      <li>Tree pruning</li>
      <li>Irrigation</li>
      <li class="tall">Weekly<br>maintenance</li>
    </ul>
    <div class="contact">
      <p class="contact__cta">Call for a free estimate</p>
      <p class="contact__heading">Contact Us:</p>
      <p class="contact__line contact__line--email">
        <svg width="16" height="11" viewBox="0 0 16 11" aria-hidden="true"><rect width="16" height="11" rx="1" fill="var(--green)"/><polyline points="1,1 8,6 15,1" fill="none" stroke="var(--black)" stroke-width="1.3"/></svg>
        hello@talbrookland.com
      </p>
      <p class="contact__line contact__line--phone">
        <svg width="16" height="16" viewBox="0 0 24 24" aria-hidden="true"><path d="M6.6 10.8a15.2 15.2 0 0 0 6.6 6.6l2.2-2.2c.3-.3.7-.4 1-.2 1.1.4 2.3.6 3.6.6.6 0 1 .4 1 1V20c0 .6-.4 1-1 1A17 17 0 0 1 3 4c0-.6.4-1 1-1h3.5c.6 0 1 .4 1 1 0 1.3.2 2.5.6 3.6.1.3 0 .7-.2 1z" fill="var(--green)"/></svg>
        123 456 7890
      </p>
      <p class="contact__social">follow us on chatlane and clipwall and roomvy</p>
    </div>
    <div class="coupon">
      <svg viewBox="0 0 160 160" width="160" height="160" aria-hidden="true">
        <polygon fill="var(--gold)" stroke="#8a5a10" stroke-width="1" points="80,2 88,20 101,5 104,25 120,13 118,33 137,26 130,44 151,42 139,58 158,63 142,74 158,84 140,92 152,107 132,109 138,128 118,124 118,145 100,134 94,154 82,138 72,157 64,138 50,153 46,133 28,141 30,121 10,122 20,104 2,97 18,86 2,74 20,66 7,51 27,49 21,30 41,35 40,14 58,24 63,5 74,20"/>
      </svg>
      <div class="coupon__text"><span class="coupon__value">10<small>%</small></span><span class="coupon__off">OFF</span></div>
    </div>
  </section>

</main>
</body>
</html>
```